Velvet Harbor Tiles Wix Website Design

We are looking for a creative Wix based website design for our new tabletop game and pop-culture collectibles company, Velvet Harbor Tiles. We are looking for something clean, simple, profession and would really like it to be as creative and original as possible. We are trying hard not to be cookie cutter and just use the standard templates. We are attaching our work-in-progress brand guide for reference. Please read though the guide as use the appropriate color pallet and fonts as per the brand guide.

Here are some similar companies in the market for reference and target the same markets as we do.

https://www.brightnook.com/
https://www.parade-fair.org/pfx
http://qz.tollmakers.com/
https://plumtarn.com/
https://www.vostrel.com/
https://www.orchardlanternplay.com/en/index/
http://www.tallpebbleyard.com/
https://www.marlowind.com/games
https://www.haybrickcraft.com/

For illustrative purposes only, please use placeholder images from similar target market websites if necessary but those will be replaced once the design has been established and before publishing.
Updates

Posting our design request during the Christmas holiday season was probably not our best idea as many of our team have not been able to participate in the feedback and evaluation processes. We would like to extend the project 5 more days in order to give the designers proper feedback on the proposals they have submitted rather than just a stars. We WILL be selecting our design choice at the end of this extension. Thanks to everyone who has already submitted. I'm confident we will have something wonderful.

Target Market(s)

Boardgamers, Gamers, Comic Books Fans, ParadeFair attendees, etc.

Number of Pages Required

3 page

Font styles to use
Sans Serif

Colors
000000
ec1f27
ffffff

Requirements
Must have
• See attached Brand Guide for color and logo references. Our company colors are Black / Red / White. Must be WIX compatible. We currently have a place holder landing page setup at www.VelvetHarborTiles.com
Nice to have
• Be creative and original.
Should not have
• no restrictions.... yet. :)

```html
<!DOCTYPE html>
<html lang="en">
<head>
<meta charset="utf-8">
<title>Velvet Harbor Tiles — The Ultimate Party Game</title>
<link rel="stylesheet" href="https://fonts.googleapis.com/css2?family=Passion+One:wght@400;700&family=Roboto:wght@400;500;700;900&display=swap">
<style>
:root{
  --red:#ec1f27;
  --red-dark:#b3080f;
  --black:#000000;
  --ink:#1d1d1d;
  --dark:#262626;
  --dark-2:#2f2f2f;
  --dark-3:#3a3a3a;
  --grey-bg:#efefef;
  --card:#f7f7f7;
  --white:#ffffff;
  --muted:#6b6b6b;
  --display:"Passion One", "Arial Black", sans-serif;
  --body:"Roboto", Arial, sans-serif;
}
*{box-sizing:border-box;margin:0;padding:0}
html,body{width:1200px;height:3364px;overflow:hidden}
body{position:relative;background:var(--white);font-family:var(--body);color:var(--ink)}
.abs{position:absolute}
.btn{position:absolute;display:flex;align-items:center;justify-content:center;background:var(--red);color:var(--white);font:700 11px/1 var(--body);letter-spacing:.5px;text-transform:uppercase}
.btn.dark{background:var(--ink)}
.display{font-family:var(--display);font-weight:700;text-transform:uppercase;line-height:.95}
.kicker{font:500 15px/1 var(--body);letter-spacing:4px}
.ruled{display:flex;align-items:center;justify-content:center;gap:14px}
.ruled::before,.ruled::after{content:"";width:30px;height:2px;background:currentColor}

/* header */
.site-header{position:absolute;left:0;top:0;width:1200px;height:61px;background:var(--white);box-shadow:0 1px 3px rgba(0,0,0,.08);z-index:2}
.nav-link{position:absolute;top:25px;font:700 12px/1 var(--body);letter-spacing:.6px;color:var(--ink);transform:translateX(-50%)}
.brand-box{position:absolute;left:541px;top:0;width:120px;height:134px;background:var(--white);box-shadow:0 1px 4px rgba(0,0,0,.15);z-index:3;display:flex;flex-direction:column;align-items:center;justify-content:center;gap:10px}
.brand-mark{width:34px;height:34px;background:var(--red)}
.brand-name{font:900 14px/1.1 var(--body);color:var(--red);text-align:center;text-transform:uppercase}
.cart{position:absolute;left:1062px;top:14px}

/* hero */
.hero{position:absolute;left:0;top:61px;width:1200px;height:544px;background:radial-gradient(ellipse at 50% 40%,#3a3a3a 0%,#1b1b1b 60%,#111 100%);color:var(--white);text-align:center}
.hero .kicker{position:absolute;top:186px;width:100%;font-size:22px;letter-spacing:6px}
.hero h1{position:absolute;top:214px;width:100%;font-size:80px}
.hero p{position:absolute;top:295px;left:270px;width:660px;font:400 17px/27px var(--body);color:#e4e4e4}
.dots{position:absolute;top:491px;left:563px;display:flex;gap:10px}
.dots span{width:11px;height:11px;border-radius:50%;background:#777}
.dots span.on{background:var(--white)}

/* perks */
.perk{position:absolute;top:605px;height:71px;display:flex;align-items:center;justify-content:center;gap:14px;color:var(--white);font:400 13px/15px var(--body)}

/* promo tiles */
.tile{position:absolute;overflow:hidden;text-align:center}
.tile-photo{position:absolute;inset:0}

/* popular */
.popular-bg{position:absolute;left:0;top:920px;width:1200px;height:643px;background:var(--grey-bg)}
.section-title{position:absolute;width:100%;text-align:center;font-size:40px}
.section-sub{position:absolute;width:100%;font:500 17px/1 var(--body);color:var(--muted)}
.offer-card{position:absolute;background:var(--card);box-shadow:0 2px 8px rgba(0,0,0,.1)}
.badge{position:absolute;width:50px;height:50px;border-radius:50%;background:var(--red);color:var(--white);display:flex;flex-direction:column;align-items:center;justify-content:center;font:700 14px/1 var(--body)}
.badge small{font-size:6px;letter-spacing:1px;margin-top:2px}

/* how to play */
.howto{position:absolute;left:0;top:1563px;width:1200px;height:535px;background:radial-gradient(ellipse at 50% 30%,#333 0%,#222 70%);color:var(--white)}
.step{position:absolute;width:220px;text-align:center;transform:translateX(-50%)}
.step-num{width:76px;height:76px;margin:0 auto;border:2px solid var(--white);border-radius:50%;display:flex;align-items:center;justify-content:center;font:700 36px/1 var(--body)}
.step h3{margin-top:28px;font:700 17px/1 var(--body)}
.step p{margin-top:14px;font:400 10.5px/18px var(--body);color:#cfcfcf}

/* featured */
.product{position:absolute;top:2259px;width:246px;height:330px;background:var(--card);box-shadow:0 1px 6px rgba(0,0,0,.08);text-align:center}
.product .art{position:absolute;left:58px;top:34px;width:130px;height:166px}
.price{position:absolute;top:216px;width:100%;font:700 19px/1 var(--body);color:var(--red)}
.pname{position:absolute;top:244px;width:100%;font:700 14px/1 var(--body);color:#333}
.pmeta{position:absolute;top:264px;width:100%;font:400 10px/1 var(--body);color:var(--muted)}
.stars{position:absolute;top:282px;width:100%;font-size:12px;letter-spacing:2px;color:#999}

/* footer */
.site-footer{position:absolute;left:0;top:3092px;width:1200px;height:272px;background:var(--ink);color:#bdbdbd}
.fcol{position:absolute;top:48px}
.fcol h4{font:700 15px/1 var(--display);color:var(--white);text-transform:uppercase;letter-spacing:.5px;margin-bottom:18px}
.fcol li{list-style:none;font:400 11px/25px var(--body)}
.legal{position:absolute;top:253px;left:182px;font:400 8px/1 var(--body);color:#9a9a9a}
.socials{position:absolute;top:248px;left:923px;display:flex;gap:8px}
.socials span{width:13px;height:13px;border-radius:50%;background:#9a9a9a}
</style>
</head>
<body>

<header class="site-header">
  <span class="nav-link" style="left:252px">ABOUT US</span>
  <span class="nav-link" style="left:405px">HOW TO PLAY</span>
  <span class="nav-link" style="left:773px">CONTACT US</span>
  <span class="nav-link" style="left:923px">MY ORDERS</span>
  <svg class="cart" width="36" height="34" viewBox="0 0 36 34" aria-label="Cart">
    <path d="M2 5h5l4 16h16l4-11H9" fill="none" stroke="#1d1d1d" stroke-width="2"/>
    <circle cx="13" cy="27" r="2.4" fill="#1d1d1d"/><circle cx="25" cy="27" r="2.4" fill="#1d1d1d"/>
    <circle cx="29" cy="6" r="6" fill="#ec1f27"/>
    <text x="29" y="9" text-anchor="middle" font-family="Roboto, sans-serif" font-size="8" font-weight="700" fill="#fff">1</text>
  </svg>
</header>
<div class="brand-box">
  <span class="brand-mark"></span>
  <span class="brand-name">Velvet Harbor<br>Tiles</span>
</div>

<section class="hero">
  <div role="img" aria-label="Background photo of friends playing a stacking block party game" style="position:absolute;inset:0"></div>
  <div class="kicker">THE ULTIMATE PARTY GAME</div>
  <h1 class="display">Velvet Harbor Tiles</h1>
  <p>Lorem ipsum dolor sit amet, consectetuer adipiscing elit. Aenean commodo ligula eget dolor. Aenean massa. Cum sociis natoque penatibus</p>
  <span class="btn" style="left:499px;top:375px;width:202px;height:39px;font-size:12px">POPULAR PRODUCTS</span>
  <div class="dots"><span></span><span></span><span class="on"></span><span></span></div>
</section>

<div class="perk" style="left:0;width:400px;background:var(--dark)">
  <svg width="44" height="30" viewBox="0 0 44 30" fill="none" stroke="#fff" stroke-width="1.6"><path d="M2 4h24v18H2zM26 10h9l6 7v5H26"/><circle cx="10" cy="24" r="3.5" fill="#262626"/><circle cx="33" cy="24" r="3.5" fill="#262626"/></svg>
  <span>Free Parcelway Ground<br>Shipping!</span>
</div>
<div class="perk" style="left:400px;width:400px;background:var(--dark-3)">
  <svg width="36" height="40" viewBox="0 0 36 40" fill="none" stroke="#fff" stroke-width="1.6"><path d="M18 2l15 6v11c0 9-7 16-15 19C10 35 3 28 3 19V8z"/><path d="M11 20l5 5 9-10"/></svg>
  <span>30 Day Money back<br>Guarantee!</span>
</div>
<div class="perk" style="left:800px;width:400px;background:var(--dark)">
  <svg width="34" height="42" viewBox="0 0 34 42" fill="none" stroke="#fff" stroke-width="1.6"><circle cx="17" cy="15" r="12"/><path d="M17 8l2.2 4.6 5 .6-3.7 3.4 1 5-4.5-2.5-4.5 2.5 1-5-3.7-3.4 5-.6z"/><path d="M9 24L4 38l6-3 3 5 3-12M25 24l5 14-6-3-3 5-3-12"/></svg>
  <span>Have 4.8 Stars Rating<br>from Clients!</span>
</div>

<!-- promo tiles -->
<div class="tile" style="left:8px;top:683px;width:590px;height:237px;background:#1e1e1e">
  <div class="tile-photo" role="img" aria-label="Wooden block tower product photo" style="left:320px;right:90px;background:linear-gradient(160deg,#d6aa6e,#a9773f)"></div>
  <div class="abs" style="left:0;top:0;width:320px;height:237px;color:var(--white)">
    <div class="kicker" style="margin-top:60px;font-size:13px;letter-spacing:3px">The Ultimate Party Game</div>
    <div class="display" style="margin-top:10px;font-size:36px">Our New Game</div>
    <div class="display ruled" style="font-size:36px">Package</div>
    <span class="btn" style="left:88px;top:158px;width:142px;height:24px;font-size:9px">WATCH NEWEST GAMES</span>
  </div>
  <div class="badge" style="left:426px;top:100px;width:72px;height:72px;font-size:22px"><small style="font-size:9px;margin:0 0 2px">From</small>$49</div>
</div>
<div class="tile" style="left:602px;top:683px;width:590px;height:237px;background:linear-gradient(135deg,#dcdcdc,#c4c4c4 50%,#e6e6e6)" role="img" aria-label="Grey marble texture background">
  <div class="display" style="margin-top:54px;font-size:46px;color:var(--ink)">Customers gave us</div>
  <div class="display ruled" style="font-size:46px;color:var(--ink)">Five stars</div>
  <span class="btn" style="left:186px;top:160px;width:196px;height:37px;font-size:11px">SEE WHAT CLIENTS SAY</span>
</div>

<!-- most popular -->
<div class="popular-bg"></div>
<h2 class="section-title display" style="top:962px">Most Popular Offer</h2>
<div class="section-sub ruled" style="top:1005px">4,8 Star Rating</div>
<span class="btn dark" style="left:834px;top:1029px;width:152px;height:31px;background:#3f3f3f;font-size:10px">LARGE 2x3 SET&nbsp;&nbsp;→</span>

<div class="offer-card" style="left:184px;top:1080px;width:804px;height:395px">
  <div class="abs" role="img" aria-label="Grey paint splash decoration" style="left:25px;top:40px;width:330px;height:300px;background:radial-gradient(ellipse,#e2e2e2 40%,transparent 70%)"></div>
  <div class="abs" role="img" aria-label="Board game box with armored heroes" style="left:88px;top:72px;width:216px;height:236px;background:var(--white);box-shadow:0 1px 5px rgba(0,0,0,.12)">
    <div style="position:absolute;left:38px;top:32px;width:140px;height:172px;background:linear-gradient(160deg,#4f6173,#2a3140)"></div>
  </div>
  <div class="badge" style="left:84px;top:56px;width:50px;height:50px">10%<small>LESS</small></div>
  <span class="abs" style="left:60px;top:170px;font-size:22px;color:#333">←</span>
  <span class="abs" style="left:333px;top:170px;font-size:22px;color:#aaa">→</span>
  <div class="abs" role="img" aria-label="Product thumbnails" style="left:172px;top:315px;display:flex;gap:10px">
    <span style="width:42px;height:40px;background:#8a6a45"></span><span style="width:42px;height:40px;background:#d9b995"></span><span style="width:42px;height:40px;background:#e6ded4"></span>
  </div>
  <div class="abs" style="left:386px;top:78px;color:var(--red);font-size:13px;letter-spacing:1px">★★★★★</div>
  <div class="abs" style="left:386px;top:102px;font:700 25px/1 var(--body);color:#333">VELVET HARBOR TILES</div>
  <div class="abs" style="left:386px;top:128px;font:700 19px/1 var(--body);color:#555">+ CASE 10 FIGURES</div>
  <p class="abs" style="left:386px;top:160px;width:365px;font:400 10.5px/20.5px var(--body);color:#555">Lorem ipsum dolor sit amet, consectetuer adipiscing elit. Aenean commodo ligula eget dolor. Aenean massa. Cum sociis natoque penatibus et magnis dis parturient montes, nascetur ridiculus mus. Donec quam felis, ultricies nec, pellentesque eu, pretium quis, sem. Nulla consequat massa quis enim. Cum soccis commodo ligula edget parturient montes.</p>
  <span class="btn" style="left:386px;top:287px;width:102px;height:27px;font-size:8.5px">ADD TO CART</span>
  <div class="abs" style="left:496px;top:287px;width:46px;height:27px;background:var(--white);border:1px solid #ddd;font:700 11px/25px var(--body);padding-left:14px">1</div>
  <div class="abs" style="left:648px;top:287px;font:700 22px/1 var(--body);color:var(--red)">$179 <s style="font-size:12px;color:#999">$249</s></div>
</div>
<div class="offer-card" style="left:1043px;top:1080px;width:200px;height:395px">
  <div class="badge" style="left:86px;top:56px;background:#d78a8d">10%<small>LESS</small></div>
  <span class="abs" style="left:62px;top:170px;font-size:22px;color:#666">←</span>
  <div class="abs" style="left:101px;top:72px;width:100px;height:236px;background:var(--white);box-shadow:0 1px 5px rgba(0,0,0,.12)"></div>
</div>

<!-- how to play -->
<section class="howto">
  <h2 class="section-title display" style="top:58px">How To Play?</h2>
  <div class="section-sub ruled" style="top:103px;color:#e8e8e8">It's 3 Easy Steps</div>
  <svg class="abs" style="left:0;top:170px" width="1200" height="120" fill="none" stroke="#777" stroke-width="1.2" stroke-dasharray="6 5">
    <path d="M340 30 C400 0 480 0 545 30"/><path d="M625 55 C700 80 780 80 840 50"/>
  </svg>
  <div class="step" style="left:300px;top:175px"><div class="step-num">1</div><h3>Select Role</h3><p>Lorem ipsum dolor sit amet, consectetuer adipiscing elit. Aenean commodo ligula eget dolor.</p></div>
  <div class="step" style="left:585px;top:175px"><div class="step-num">2</div><h3>Select Level up</h3><p>Lorem ipsum dolor sit amet, consectetuer adipiscing elit. Aenean commodo ligula eget dolor.</p></div>
  <div class="step" style="left:879px;top:175px"><div class="step-num">3</div><h3>Play the Game</h3><p>Lorem ipsum dolor sit amet, consectetuer adipiscing elit. Aenean commodo ligula eget dolor.</p></div>
  <span class="btn" style="left:492px;top:417px;width:191px;height:36px">CUSTOMIZE TOWER</span>
</section>

<!-- featured -->
<h2 class="section-title display" style="top:2161px">Featured Products</h2>
<div class="section-sub ruled" style="top:2204px">Products Just Reached us</div>

<div class="product" style="left:73px">
  <div class="art" role="img" aria-label="Hollow Crest game box" style="background:linear-gradient(160deg,#4f6173,#2a3140)"></div>
  <div class="price">$169.99</div><div class="pname">HOLLOW CREST FULL SET</div><div class="pmeta">For 2-7 People</div><div class="stars">★★★★<span style="color:#ccc">★</span></div>
</div>
<div class="product" style="left:341px">
  <div class="art" role="img" aria-label="Rumble Stack game box" style="background:linear-gradient(160deg,#c23a1c,#5a2d1a)"></div>
  <div class="price">$170.99</div><div class="pname">RUMBLE STACK SET</div><div class="pmeta">Up to 15 people</div><div class="stars">★★★★<span style="color:#ccc">★</span></div>
</div>
<div class="product" style="left:610px">
  <div class="art" role="img" aria-label="Hollow Crest game box" style="background:linear-gradient(160deg,#4f6173,#2a3140)"></div>
  <div class="price">$169.99</div><div class="pname">HOLLOW CREST FULL SET</div><div class="pmeta">For 2-7 People</div><div class="stars">★★★★<span style="color:#ccc">★</span></div>
</div>
<div class="product" style="left:879px">
  <div class="art" role="img" aria-label="Rumble Stack game box" style="background:linear-gradient(160deg,#c23a1c,#5a2d1a)"></div>
  <div class="price">$170.99</div><div class="pname">RUMBLE STACK SET</div><div class="pmeta">Up to 15 people</div><div class="stars">★★★★<span style="color:#ccc">★</span></div>
</div>
<div class="badge" style="left:1075px;top:2245px;width:58px;height:58px;font-size:15px">30%<small>LESS</small></div>
<span class="btn" style="left:505px;top:2634px;width:186px;height:36px">SHOW ALL PRODUCTS</span>

<!-- closing promos -->
<div class="tile" style="left:0;top:2729px;width:599px;height:355px;background:linear-gradient(135deg,#3a3431,#6b4a32 55%,#2a2522)" role="img" aria-label="Photo of a hand pulling a block from a wooden tower">
  <div class="kicker" style="margin-top:107px;font-size:18px;letter-spacing:5px;color:var(--white)">The Ultimate Party Game</div>
  <div class="display" style="margin-top:12px;font-size:52px;color:var(--white)">Branded Harbor</div>
  <div class="display ruled" style="font-size:52px;color:var(--white)">Games</div>
  <span class="btn" style="left:176px;top:240px;width:197px;height:39px;font-size:12px">SHOW ALL PRODUCTS</span>
</div>
<div class="tile" style="left:607px;top:2729px;width:593px;height:355px;background:radial-gradient(ellipse at 50% 45%,#f02a31,#c00d14 75%)">
  <div class="kicker" style="margin-top:107px;font-size:18px;letter-spacing:5px;color:var(--white)">The Ultimate Party Game</div>
  <div class="display" style="margin-top:12px;font-size:52px;color:var(--white)">45% Off for all</div>
  <div class="display ruled" style="font-size:52px;color:var(--white)">Our Games</div>
  <span class="btn dark" style="left:200px;top:240px;width:195px;height:39px;font-size:12px">SHOW ALL PRODUCTS</span>
</div>

<footer class="site-footer">
  <div class="fcol" style="left:182px"><h4>Navigation</h4><ul><li>Who we are</li><li>What we do</li><li>Features</li><li>Architecture</li><li>Core Team</li></ul></div>
  <div class="fcol" style="left:411px;top:45px"><h4>Policy</h4><ul><li>Conditions &amp; Terms</li><li>About us</li><li>Privacy Policy</li><li>Write to us</li><li>Block Security</li></ul></div>
  <div class="fcol" style="left:649px;top:45px"><h4>Contacts</h4><ul><li>Your Street Adress</li><li>Phone Numbers</li><li>Email Addresses</li><li>Working Hours</li><li>Products</li></ul></div>
  <div class="fcol" style="left:875px;top:45px"><h4>Subscribe</h4>
    <div style="width:152px;height:24px;background:#e8e8e8;font:400 9px/24px var(--body);color:#888;padding-left:12px">Email Address</div>
    <div style="margin-top:8px;width:64px;height:19px;background:var(--red);color:var(--white);font:400 8px/19px var(--body);text-align:center">Submit</div>
  </div>
  <div class="abs" style="left:0;top:235px;width:1200px;height:1px;background:#3a3a3a"></div>
  <div class="legal">Conditions &amp; Terms &nbsp;|&nbsp; Privacy Policy &nbsp;|&nbsp; All rights reserverd 2018</div>
  <div class="socials"><span></span><span></span><span></span><span></span><span></span></div>
</footer>

</body>
</html>
```